Label for Whiskey and Rum Bottle

We are a distillery. Whiskey and Rum We like to have a new label for our bottles. The whiskey bottles are in a wooden case. http://www.korntropfen-muster.ch/store/product/tannwalder-oberkamm-single-malt-whiskey-nr-6 The Rum Bottles have no package. The label is even more important. http://www.korntropfen-muster.ch/store/product/tannwalder-oberkämmer-rum You can see the form of the bottles here www.korntropfen-muster.ch/store Whiskey and rum bottles are for a liter (50 cl) The labels can be with a picture or without. We would like to have something completely new. Therefore we don`t like to make much prescriptions concerning the design. We don`t like to give too much information (text) on the label. Just the information required by law. Consumers should understand the labels without long-reading. (The label-text is below) The 2 labels (Whiskey and rum) should look similar. Probably they have a different color or a different picture or .... It should be clear that the 2 products are from the same distillery. We have the intention to change all our existing labels over time. This gives designers the chance for follow-up projects.

Target Market(s)

Adults, liquor lovers

Requirements
Must have
• Information on the label is in German. (See "") Whiskey: - the name of the whiskey is "Tannwald Ridgeside Single Malt Whiskey" - The Whiskey was matured 5 years in a sherry "5 years in the sherry barrel stored" - The Alcohol content is 40% volumes "40% Vol "- The bottle contents 50 cl" 5 dl "- The distillery is" Distillery Brugghofer, Felsmatt, www.korntropfen-muster.ch "- The producer is" Korvix GmbH "Rum: - The name is" Tannwald Ridgesider Rum "- The alcohol content is 37% Volumes "37% Vol" - The bottle contens 50 cl "5 dl" - The distillery is "Distillery Brugghofer, Felsmatt, www.korntropfen-muster.ch" - The producer is "Korvix GmbH"
Nice to have
• Premium looking label Only front label preferred Only necessary text on the label
Should not have
• No special print techniques necessary No special paper form

```html
<!DOCTYPE html>
<html lang="de">
<head>
<meta charset="utf-8">
<title>Brugghofer – Etiketten Whiskey &amp; Rum</title>
<link rel="stylesheet" href="https://fonts.googleapis.com/css2?family=Open+Sans:wght@400;600&family=Silkscreen:wght@700&display=swap">
<style>
  :root {
    --bg: #e4e3e2;
    --label-black: #1b1b1b;
    --whiskey-light: #ffb22e;
    --whiskey-deep: #e07a10;
    --rum-light: #ff9a2a;
    --rum-deep: #e2560f;
    --accent: #f29a1d;
    --white: #f4f4f4;
    --ink: #141414;
  }
  * { box-sizing: border-box; margin: 0; padding: 0; }
  html, body { width: 1200px; height: 600px; overflow: hidden; }
  body {
    background: var(--bg);
    display: flex;
    align-items: center;
    justify-content: space-around;
    font-family: "Open Sans", Arial, sans-serif;
  }
  .label {
    position: relative;
    width: 340px;
    height: 440px;
    color: var(--white);
    box-shadow: 0 10px 30px rgba(0,0,0,.18);
  }
  .label--rum { --accent: #f07a1e; }
  .label__ground { position: absolute; inset: 0; width: 100%; height: 100%; }
  .brand {
    position: absolute; left: 0; right: 0; top: 34px;
    text-align: center;
    font-family: "Open Sans", Arial, sans-serif;
    font-weight: 600; font-size: 15px; line-height: 1;
    letter-spacing: .18em; text-transform: uppercase;
    color: var(--ink);
    padding-right: 60px;
  }
  .product {
    position: absolute; top: 150px; left: 0; right: 0;
    text-align: center;
  }
  .product__name {
    display: inline-block;
    font-family: "Silkscreen", "Courier New", monospace;
    font-weight: 700; font-size: 40px; line-height: 1;
    padding: 6px 12px 4px;
    border: 3px solid var(--accent);
    letter-spacing: .04em;
    background: var(--label-black);
  }
  .product__sub {
    margin-top: 10px; font-size: 13px; font-weight: 600;
  }
  .aging {
    position: absolute; top: 238px; left: 40px; right: 40px;
    display: flex; align-items: center; gap: 8px;
    font-size: 10.5px; color: var(--accent); white-space: nowrap;
  }
  .aging::before, .aging::after {
    content: ""; flex: 1; height: 1px; background: var(--accent);
  }
  .abv { position: absolute; top: 262px; left: 50%; width: 86px; height: 96px; transform: translateX(-50%); }
  .bars {
    position: absolute; right: 20px; top: 300px;
    display: flex; flex-direction: column; gap: 7px;
  }
  .bars span { display: block; width: 34px; height: 8px; background: var(--accent); }
  .maker {
    position: absolute; left: 18px; bottom: 22px;
    font-size: 11px; line-height: 1.5; font-weight: 600;
  }
  .maker__key, .maker__place { color: var(--accent); }
  .volume {
    position: absolute; right: 22px; bottom: 30px;
    font-size: 18px; color: var(--accent);
  }
</style>
</head>
<body>

<article class="label label--whiskey">
  <svg class="label__ground" viewBox="0 0 340 440" preserveAspectRatio="none" aria-hidden="true">
    <defs>
      <linearGradient id="whiskey-band" x1="0" y1="0" x2="1" y2="1">
        <stop offset="0" stop-color="var(--whiskey-light)"/>
        <stop offset="1" stop-color="var(--whiskey-deep)"/>
      </linearGradient>
    </defs>
    <rect width="340" height="440" fill="url(#whiskey-band)"/>
    <path d="M0 122 C130 112 260 80 340 18 L340 440 L0 440 Z" fill="var(--label-black)"/>
  </svg>
  <p class="brand">Brugghofer</p>
  <div class="product">
    <h1 class="product__name">Whiskey</h1>
    <p class="product__sub">Tannwalder Oberkamm Single Malt Whiskey</p>
  </div>
  <p class="aging">5 Jahre im Sherry Fass gelagert</p>
  <svg class="abv" viewBox="0 0 86 96" aria-label="40 % Vol Alcohol Content">
    <path d="M43 6 C52 22 64 32 64 48 A21 21 0 0 1 22 48 C22 32 34 22 43 6 Z" fill="var(--accent)"/>
    <text x="43" y="47" text-anchor="middle" font-size="10" font-weight="600" fill="#1b1b1b">40 %</text>
    <text x="43" y="58" text-anchor="middle" font-size="9" font-weight="600" fill="#1b1b1b">VOL</text>
    <path id="arc-w" d="M14 58 A29 29 0 0 0 72 58" fill="none"/>
    <text font-size="6.5" font-weight="600" fill="#f4f4f4" letter-spacing="1"><textPath href="#arc-w" startOffset="50%" text-anchor="middle">ALCOHOL CONTENT</textPath></text>
  </svg>
  <div class="bars"><span></span><span></span><span></span></div>
  <p class="maker">
    <span class="maker__key">PRODUCED BY :</span> Korvix GmbH<br>
    <span class="maker__place">Brennerei Brugghofer, Felsmatt</span><br>
    www.korntropfen-muster.ch
  </p>
  <p class="volume">5 dl</p>
</article>

<article class="label label--rum">
  <svg class="label__ground" viewBox="0 0 340 440" preserveAspectRatio="none" aria-hidden="true">
    <defs>
      <linearGradient id="rum-band" x1="0" y1="0" x2="1" y2="1">
        <stop offset="0" stop-color="var(--rum-light)"/>
        <stop offset="1" stop-color="var(--rum-deep)"/>
      </linearGradient>
    </defs>
    <rect width="340" height="440" fill="url(#rum-band)"/>
    <path d="M0 122 C130 112 260 80 340 18 L340 440 L0 440 Z" fill="var(--label-black)"/>
  </svg>
  <p class="brand">Brugghofer</p>
  <div class="product">
    <h1 class="product__name">Rum</h1>
  </div>
  <p class="aging">5 Jahre im Sherry Fass gelagert</p>
  <svg class="abv" viewBox="0 0 86 96" aria-label="37 % Vol Alcohol Content">
    <path d="M43 6 C52 22 64 32 64 48 A21 21 0 0 1 22 48 C22 32 34 22 43 6 Z" fill="var(--accent)"/>
    <text x="43" y="47" text-anchor="middle" font-size="10" font-weight="600" fill="#1b1b1b">37 %</text>
    <text x="43" y="58" text-anchor="middle" font-size="9" font-weight="600" fill="#1b1b1b">VOL</text>
    <path id="arc-r" d="M14 58 A29 29 0 0 0 72 58" fill="none"/>
    <text font-size="6.5" font-weight="600" fill="#f4f4f4" letter-spacing="1"><textPath href="#arc-r" startOffset="50%" text-anchor="middle">ALCOHOL CONTENT</textPath></text>
  </svg>
  <div class="bars"><span></span><span></span><span></span></div>
  <p class="maker">
    <span class="maker__key">PRODUCED BY :</span> Korvix GmbH<br>
    <span class="maker__place">Brennerei Brugghofer, Felsmatt</span><br>
    www.korntropfen-muster.ch
  </p>
  <p class="volume">5 dl</p>
</article>

</body>
</html>
```